Visitenkarten-Design für K17.eu - TradeWing Finanz
Zielgruppe
Smartphone-Banking mit Mehrwert
Aufgabenstellung
Bitte entwerfen Sie kreative Visitenkarten für uns.
- Halten Sie einen Platz/Rahmen frei für Fotos, die wir nachträglich einsetzen, und kennzeichnen diesen.
- Halten Sie einen Patz/Rahmen für Vor- und Nachname sowie für die Berufsbezeichnung frei und kennzeichnen diesen.
- Halten Sie einen Platz/Rahmen für die Telefonnummern und die Email-Adressen frei und kennzeichnen diesen.
Alle Visitenkarten sollen folgende Daten beinhalten:
Vorname Nachname*
Berufsbezeichnung*
Mobile:
Office:
Email:
Domain:
* = individuell, jeder Mitarbeiter hat eigene Daten
Die Farben müssen sich an unserem CI-Design orientieren, orange/weiß/schwarz/grau -
Außerdem finden Sie unser Logo in der Anlage, welches Sie bitte auf der Karte platzieren.
Bitte liefern Sie uns die Designs in verschiedenen Formaten - psd, ai, eps, jpg, png
Bei Fragen zögern Sie nicht, uns zu kontaktieren. Danke.

```html
<!DOCTYPE html>
<html lang="de">
<head>
<meta charset="utf-8">
<title>K17.eu – Visitenkarten</title>
<link href="https://fonts.googleapis.com/css2?family=Arimo:wght@400;700&display=swap" rel="stylesheet">
<style>
  :root {
    --bg: #dcdcdc;
    --card: #ffffff;
    --orange: #e07b2e;
    --orange-light: #eea266;
    --orange-pale: #f4c39b;
    --grey: #5f5f5f;
    --grey-dark: #3d3d3d;
    --device: #1c1c1c;
  }
  * { margin: 0; padding: 0; box-sizing: border-box; }
  html, body { width: 1200px; height: 873px; overflow: hidden; }
  body {
    background: var(--bg);
    font-family: "Arimo", Arial, sans-serif;
    color: var(--grey);
    position: relative;
  }
  .card {
    position: absolute;
    width: 520px;
    height: 336px;
    background: var(--card);
    overflow: hidden;
    box-shadow: 0 6px 18px rgba(0,0,0,0.18);
  }
  .card--front { left: 50px; top: 268px; }
  .card--back  { left: 630px; top: 268px; }

  .wave-band { position: absolute; left: 0; bottom: 0; width: 520px; height: 336px; }

  .brand-small { position: absolute; left: 28px; top: 20px; line-height: 1; }
  .brand-small .brand-name { font-weight: 700; font-size: 22px; color: var(--orange); }
  .brand-small .brand-url { font-size: 10px; color: var(--grey-dark); margin-top: 3px; font-weight: 700; }

  .device {
    position: absolute; left: 30px; top: 74px;
    width: 200px; height: 104px;
    border-radius: 16px;
    background: var(--device);
    padding: 9px 24px 9px 34px;
  }
  .photo-slot {
    width: 100%; height: 100%;
    border-radius: 2px;
    background: linear-gradient(120deg, #4a3a30 0%, #8a6a55 45%, #d9d4d0 100%);
  }

  .contact { position: absolute; left: 258px; top: 96px; }
  .contact .person-name { color: var(--orange); font-size: 17px; }
  .contact .person-role { font-size: 13px; margin-top: 3px; }
  .contact .address { font-size: 13px; line-height: 1.3; margin-top: 16px; }
  .contact .lines { margin-top: 14px; font-size: 13px; line-height: 1.35; }
  .contact .row { display: flex; align-items: flex-start; gap: 10px; }
  .contact .icon { width: 26px; flex: none; }

  .brand-large { position: absolute; left: 0; right: 0; top: 110px; text-align: center; line-height: 1; }
  .brand-large .brand-name { font-weight: 700; font-size: 76px; color: var(--orange); }
  .brand-large .brand-url { font-weight: 700; font-size: 26px; color: var(--grey); margin-top: 8px; }
</style>
</head>
<body>

<section class="card card--front">
  <svg class="wave-band" viewBox="0 0 520 336" aria-hidden="true">
    <path d="M0 150 C40 170 60 210 110 230 C180 258 260 262 330 290 C400 316 470 318 520 326 L520 336 L0 336 Z" fill="var(--orange-pale)"/>
    <path d="M0 175 C50 200 80 235 150 250 C230 268 300 280 380 305 C440 322 490 326 520 330 L520 336 L0 336 Z" fill="var(--orange-light)"/>
    <path d="M0 205 C60 230 110 262 190 275 C270 290 340 305 420 322 C470 330 500 333 520 334 L520 336 L0 336 Z" fill="var(--orange)"/>
  </svg>

  <div class="brand-small">
    <div class="brand-name">K17</div>
    <div class="brand-url">www.k17.eu</div>
  </div>

  <div class="device">
    <div class="photo-slot" role="img" aria-label="Platzhalter für Mitarbeiterfoto auf Smartphone-Bildschirm"></div>
  </div>

  <div class="contact">
    <div class="person-name">Vorname Nachname</div>
    <div class="person-role">Berufsbezeichnung</div>
    <div class="address">Lindenweg 12<br>94036 Ostheim<br>Germany</div>
    <div class="lines">
      <div class="row">
        <svg class="icon" width="26" height="34" viewBox="0 0 26 34" aria-hidden="true">
          <rect x="2" y="2" width="22" height="30" rx="3" fill="none" stroke="var(--orange)" stroke-width="2"/>
          <line x1="2" y1="8" x2="24" y2="8" stroke="var(--orange)" stroke-width="1.5"/>
          <line x1="2" y1="26" x2="24" y2="26" stroke="var(--orange)" stroke-width="1.5"/>
        </svg>
        <div>+49 171 xxxxxxx<br>+49 841 xxxxxx-xx</div>
      </div>
      <div class="row" style="margin-top:4px">
        <svg class="icon" width="26" height="18" viewBox="0 0 26 18" aria-hidden="true">
          <rect x="1.5" y="1.5" width="23" height="15" fill="none" stroke="var(--orange)" stroke-width="2"/>
          <path d="M1.5 1.5 L24.5 16.5 M24.5 1.5 L1.5 16.5" stroke="var(--orange)" stroke-width="1.5"/>
        </svg>
        <div>vorname@k17.eu</div>
      </div>
    </div>
  </div>
</section>

<section class="card card--back">
  <div class="brand-large">
    <div class="brand-name">K17</div>
    <div class="brand-url">www.k17.eu</div>
  </div>
</section>

</body>
</html>
```